Design a Web Development Agency Website

This project is to design a website for a Web Development Agency named Mavorix.
Please design the landing page first and if your design is selected then you can design the Services, About Us, and Portfolio page.
This web agency is targeted to the African market specifically small businesses in Nigeria so the design should be modern, professional, clean and elegant.

The name of the company as shall appear in the footer is Mavorix Communications Ltd.

Industry/Entity Type

Web design, small to med sized business

Number of Pages Required

4 page

Font styles to use
Sans Serif

Colors
00AB8E
00BBA5
67D7C9
C6EFE9
E9F9F6
F0912C
F2A743
F7CA91
FBE8D2
FDF5EE

Requirements
Must have
• Professional, clean home page, MUST deliver in Figma

```html
<!DOCTYPE html>
<html lang="en">
<head>
<meta charset="utf-8">
<title>Mavorix Communications Ltd</title>
<link href="https://fonts.googleapis.com/css2?family=Montserrat:wght@400;500;600;700&display=swap" rel="stylesheet">
<style>
:root{
  --teal:#00AB8E;
  --teal-2:#00BBA5;
  --teal-band:#14a391;
  --teal-dark:#0d4f4c;
  --teal-pale:#E9F9F6;
  --orange:#F0912C;
  --orange-2:#F2A743;
  --ink:#1b1b1b;
  --navy:#143b5c;
  --body:#6f6f6f;
  --line:#e1e1e1;
  --grey-bg:#f7f7f7;
  --white:#ffffff;
}
*{margin:0;padding:0;box-sizing:border-box}
html,body{width:1200px;height:4415px;overflow:hidden}
body{font-family:"Montserrat",sans-serif;color:var(--ink);background:var(--white);position:relative}
.abs{position:absolute}
a{text-decoration:none;color:inherit}

/* hero */
.hero{left:0;top:0;width:1200px;height:571px;background:linear-gradient(100deg,#0f5a55 0%,#1d5e63 45%,#2f6a72 70%,#1c4f55 100%);overflow:hidden}
.hero-wave{left:0;top:520px;width:1200px;height:60px}
.brand{left:115px;top:24px;color:var(--white)}
.brand-name{font-size:25px;font-weight:700;letter-spacing:.5px;line-height:1}
.brand-sub{font-size:12px;font-weight:500;letter-spacing:.6px;margin-top:2px}
.nav{top:28px;left:608px;display:flex;align-items:center;gap:0;color:var(--white);font-size:13.5px}
.nav a{margin-right:40px}
.nav .nav-cta{background:rgba(255,255,255,.12);padding:9px 14px;margin-right:0;border-radius:2px}
.hero-kicker{left:115px;top:177px;color:var(--white);font-size:13.5px}
.hero-title{left:115px;top:213px;color:var(--white);font-size:41px;font-weight:600;line-height:51px;width:560px}
.btn{display:inline-flex;align-items:center;justify-content:center;font-weight:500;font-size:13px;color:var(--white);border-radius:2px}
.btn-orange{background:var(--orange);box-shadow:0 3px 0 #c9701a}
.hero-btn{left:115px;top:413px;width:148px;height:42px}
.hero-reviews{left:294px;top:424px;color:var(--white);font-size:13px;display:flex;align-items:center;gap:8px}

/* logos */
.seen{left:0;top:629px;width:1200px;text-align:center;font-size:12.5px;font-weight:500}
.logos{left:115px;top:668px;width:955px;display:flex;justify-content:space-between;align-items:center}
.logo{display:flex;align-items:center;gap:8px;font-size:20px;font-weight:700;color:#2b2b2b}
.logo i{display:block;width:20px;height:20px;border-radius:50%;background:#2b2b2b}

/* grid deco */
.grid{background-image:linear-gradient(#eee 1px,transparent 1px),linear-gradient(90deg,#eee 1px,transparent 1px);background-size:17px 17px;opacity:.6}

/* about */
.photo{border-radius:4px}
.about-1{left:115px;top:797px;width:180px;height:189px;background:linear-gradient(135deg,#d9d4c9,#7d776c 70%,#3e3a35)}
.about-2{left:115px;top:998px;width:180px;height:200px;background:linear-gradient(160deg,#6d8ea3,#2d3f4c 60%,#bfa58f)}
.about-3{left:305px;top:828px;width:225px;height:334px;background:linear-gradient(160deg,#58748c,#2c3743 50%,#8e6a4f)}
.about-title{left:603px;top:868px;font-size:29px;font-weight:600;line-height:37px}
.about-text{left:603px;top:956px;width:395px;font-size:12.5px;line-height:20.5px;color:var(--body)}
.btn-teal{background:var(--teal);gap:10px}
.about-btn{left:603px;top:1097px;width:132px;height:35px}
.about-btn span.circ{width:16px;height:16px;border-radius:50%;border:1px solid rgba(255,255,255,.7);display:inline-flex;align-items:center;justify-content:center}

/* services */
.services{left:0;top:1268px;width:1200px;height:678px;background:var(--grey-bg)}
.sec-title{left:0;width:1200px;text-align:center;font-size:29px;font-weight:600}
.sec-text{left:300px;width:600px;text-align:center;font-size:12.5px;line-height:20.5px;color:#444}
.card{width:473px;height:163px;border:2px solid var(--line);background:transparent;border-radius:3px}
.card-icon{position:absolute;left:-6px;top:-18px;width:46px;height:46px;background:var(--grey-bg)}
.card h3{position:absolute;left:27px;top:36px;font-size:14.5px;font-weight:600}
.card p{position:absolute;left:27px;top:66px;width:410px;font-size:12.5px;line-height:20.5px;color:var(--body)}
.card .more{position:absolute;left:27px;top:115px;font-size:12.5px;color:var(--orange);border-bottom:1px solid var(--orange);padding-bottom:2px}

/* cta band */
.cta{left:0;top:1946px;width:1200px;height:365px;background:linear-gradient(180deg,var(--teal-band),#12a08e);color:var(--white);text-align:center}
.cta-kicker{top:94px;width:1200px;font-size:12.5px}
.cta-title{top:114px;width:1200px;font-size:30px;font-weight:600}
.cta-text{top:162px;left:350px;width:500px;font-size:12.5px;line-height:20.5px}
.cta-btn{left:549px;top:238px;width:102px;height:35px}

/* testimonial */
.quote-mark{left:113px;top:2428px;color:var(--teal);font-size:44px;font-weight:700;line-height:1}
.quote-text{left:115px;top:2474px;width:440px;font-size:21px;font-weight:700;line-height:34px;color:var(--navy)}
.quote-name{left:113px;top:2593px;font-size:12.5px}
.dots{left:115px;top:2656px;display:flex;gap:7px}
.dots i{width:6px;height:6px;border-radius:50%;background:#ddd}
.dots i.on{background:var(--teal)}
.avatar{left:809px;top:2455px;width:82px;height:82px;border-radius:50%;background:linear-gradient(160deg,#7fcfe0,#3aa6c3)}
.reviewer{left:720px;top:2557px;width:340px;text-align:center;font-size:11.5px;line-height:18px;color:#555}
.reviewer b{font-weight:500;color:var(--ink)}
.rev-link{left:791px;top:2603px;display:flex;align-items:center;gap:8px;font-size:13px}

/* case studies */
.cases-bg{left:0;top:2760px;width:1200px;height:785px;background:var(--grey-bg)}
.tabs{left:270px;top:3016px;display:flex;gap:48px;font-size:15px;color:#9a9a9a}
.tabs .active{color:var(--navy);border-bottom:2px solid var(--teal);padding-bottom:5px}
.shot{top:3079px;width:225px;height:308px;box-shadow:0 8px 20px rgba(0,0,0,.12)}
.arrows{left:118px;top:3426px;display:flex;gap:24px}

/* contact */
.contact-title{left:199px;top:3688px;font-size:31px;font-weight:600;line-height:39px}
.contact-text{left:199px;top:3780px;width:385px;font-size:12.5px;line-height:20.5px;color:var(--body)}
.contact-btn{left:199px;top:3895px;width:149px;height:41px}
.c-photo-1{left:753px;top:3656px;width:330px;height:232px;background:linear-gradient(120deg,#e8ecef,#c9d3da 50%,#3b4a6b)}
.c-photo-2{left:648px;top:3843px;width:279px;height:177px;background:linear-gradient(120deg,#c9a98a,#6c4a35 55%,#d8d8d8)}

/* footer */
.footer{left:0;top:4080px;width:1200px;height:335px;background:var(--teal-band);border-top-left-radius:150px 100px;color:var(--white)}
.f-brand{left:115px;top:70px}
.f-brand .brand-name{font-size:25px}
.f-tag{left:115px;top:147px;width:250px;font-size:12.5px;font-weight:700;line-height:20.5px}
.f-col h4{font-size:13px;font-weight:600;margin-bottom:14px}
.f-col a{display:block;font-size:12.5px;line-height:26px}
.copy{left:115px;top:4368px;font-size:10px;color:var(--white)}
.copy u{text-decoration:underline}
.social{left:972px;top:4366px;display:flex;gap:11px}
.social i{width:20px;height:20px;border-radius:50%;background:rgba(255,255,255,.35)}
</style>
</head>
<body>

<!-- Hero -->
<section class="abs hero" role="img" aria-label="Photo of a man working at computer screens in an office, under a dark teal tint">
  <svg class="abs hero-wave" viewBox="0 0 1200 60" preserveAspectRatio="none"><path d="M0 35 Q300 10 620 28 T1200 15 V60 H0Z" fill="#e9f9f6"/><path d="M0 42 Q300 20 620 36 T1200 28 V60 H0Z" fill="#ffffff"/></svg>
</section>
<div class="abs brand"><div class="brand-name">MAVORIX</div><div class="brand-sub">Communications Ltd</div></div>
<nav class="abs nav"><a>Home</a><a>About Us</a><a>Services</a><a>Portfolio</a><a class="nav-cta">Contact Us</a></nav>
<p class="abs hero-kicker">Welcome to Mavorix Communications</p>
<h1 class="abs hero-title">We have the latest knowledge to support your commercial goals</h1>
<a class="abs btn btn-orange hero-btn">Contact Our Team</a>
<a class="abs hero-reviews"><svg width="16" height="14" viewBox="0 0 16 14"><path d="M1 1h14v9H5l-4 3z" fill="#fff"/><path d="M4 4h8M4 7h6" stroke="#1d5e63" stroke-width="1.2"/></svg>Read Reviews</a>

<!-- As seen on -->
<p class="abs seen">As Seen On:</p>
<div class="abs logos">
  <div class="logo"><i></i>Northpeak</div>
  <div class="logo">Helvane</div>
  <div class="logo">Corvita</div>
  <div class="logo">Lumari</div>
  <div class="logo">Ostrell</div>
  <div class="logo">Verdalis</div>
</div>

<!-- About -->
<div class="abs grid" style="left:280px;top:722px;width:360px;height:300px"></div>
<div class="abs photo about-1" role="img" aria-label="Design sketches on a desk with coffee cups"></div>
<div class="abs photo about-2" role="img" aria-label="Hands typing on a laptop keyboard"></div>
<div class="abs photo about-3" role="img" aria-label="Team gathered around a computer screen"></div>
<h2 class="abs about-title">About Mavorix<br>Communications Ltd</h2>
<p class="abs about-text">Lorem ipsum dolor sit amet, consectetur adipiscing elit. Est vitae, pellentesque cum in etiam ultrices. Neque egestas velit facilisis at dolor at. Accumsan, arcu massa tellus tempus, aenean purus viverra. Commodo sed mauris ultrices quam urna. Nisi, ullamcorper id aliquet sem condimentum massa eu.</p>
<a class="abs btn btn-teal about-btn">Learn More <span class="circ"><svg width="8" height="8" viewBox="0 0 8 8"><path d="M1 4h6M4.5 1.5 7 4 4.5 6.5" stroke="#fff" fill="none"/></svg></span></a>

<!-- Services -->
<section class="abs services">
  <h2 class="abs sec-title" style="top:74px">Services We Offer</h2>
  <p class="abs sec-text" style="top:123px">Accumsan, arcu massa tellus tempus, aenean purus viverra. Commodo sed mauris ultrices quam urna. Nisi, ullamcorper id aliquet sem condimentum massa eu.</p>

  <div class="abs card" style="left:115px;top:211px">
    <svg class="card-icon" viewBox="0 0 46 46"><rect x="8" y="5" width="30" height="24" rx="2" fill="none" stroke="#1d6e79" stroke-width="2"/><path d="M4 33h38v4H4z" fill="#1d6e79"/><path d="M19 12l-4 5 4 5M27 12l4 5-4 5" stroke="#F0912C" stroke-width="2" fill="none"/></svg>
    <h3>Software Development</h3>
    <p>Lorem ipsum dolor sit amet, consectetur adipiscing elit. Est vitae, pellentesque cum in etiam ultrices.</p>
    <a class="more">Read More →</a>
  </div>
  <div class="abs card" style="left:610px;top:211px">
    <svg class="card-icon" viewBox="0 0 46 46"><rect x="6" y="6" width="34" height="26" rx="2" fill="none" stroke="#1d6e79" stroke-width="2"/><path d="M6 12h34" stroke="#1d6e79" stroke-width="2"/><path d="M18 28l5-10 5 10z" fill="#F0912C"/></svg>
    <h3>UX Design</h3>
    <p>Lorem ipsum dolor sit amet, consectetur adipiscing elit. Est vitae, pellentesque cum in etiam ultrices.</p>
    <a class="more">Read More →</a>
  </div>
  <div class="abs card" style="left:115px;top:405px">
    <svg class="card-icon" viewBox="0 0 46 46"><rect x="16" y="6" width="16" height="30" rx="2" fill="none" stroke="#1d6e79" stroke-width="2"/><rect x="4" y="16" width="12" height="10" fill="#67D7C9"/><circle cx="38" cy="26" r="5" fill="#F0912C"/></svg>
    <h3>Mobile App</h3>
    <p>Lorem ipsum dolor sit amet, consectetur adipiscing elit. Est vitae, pellentesque cum in etiam ultrices.</p>
    <a class="more">Read More →</a>
  </div>
  <div class="abs card" style="left:610px;top:405px">
    <svg class="card-icon" viewBox="0 0 46 46"><path d="M8 36V26M16 36V20M24 36V24" stroke="#1d6e79" stroke-width="4"/><circle cx="33" cy="14" r="7" fill="none" stroke="#1d6e79" stroke-width="2"/><circle cx="33" cy="14" r="3" fill="#F0912C"/></svg>
    <h3>SEO</h3>
    <p>Lorem ipsum dolor sit amet, consectetur adipiscing elit. Est vitae, pellentesque cum in etiam ultrices.</p>
    <a class="more">Read More →</a>
  </div>
</section>

<!-- Call to action -->
<section class="abs cta">
  <p class="abs cta-kicker">→&nbsp;&nbsp;Lets Get Started</p>
  <h2 class="abs cta-title">Do you have questions? Contact Us</h2>
  <p class="abs cta-text">Lorem ipsum dolor sit amet, consectetur adipiscing elit. Est vitae, pellentesque cum in etiam ultrices.</p>
  <a class="abs btn btn-orange cta-btn">Contact Us</a>
</section>

<!-- Testimonial -->
<div class="abs grid" style="left:660px;top:2370px;width:390px;height:360px"></div>
<div class="abs quote-mark">“</div>
<blockquote class="abs quote-text">Lorem ipsum dolor sit amet, consectetur adipiscing elit. Est vitae, pellentesque cum in etiam ultrices</blockquote>
<p class="abs quote-name">John Doe</p>
<div class="abs dots"><i></i><i class="on"></i><i></i><i></i></div>
<div class="abs avatar" role="img" aria-label="Portrait of the reviewer"></div>
<p class="abs reviewer"><b>John Doe</b> Lorem ipsum dolor sit amet,<br>consectetur adipiscing elit</p>
<a class="abs rev-link"><svg width="16" height="14" viewBox="0 0 16 14"><path d="M1 1h14v9H5l-4 3z" fill="#00AB8E"/><path d="M4 4h8M4 7h6" stroke="#fff" stroke-width="1.2"/></svg>Read Reviews</a>

<!-- Case studies -->
<svg class="abs" style="left:0;top:2745px" width="1200" height="80" viewBox="0 0 1200 80" preserveAspectRatio="none"><path d="M0 50 Q600 -10 1200 30 V80 H0Z" fill="#ececec"/><path d="M0 60 Q600 5 1200 45 V80 H0Z" fill="#f7f7f7"/></svg>
<section class="abs cases-bg" style="top:2815px;height:730px"></section>
<h2 class="abs sec-title" style="top:2850px">Our Case Studies</h2>
<p class="abs sec-text" style="left:300px;top:2906px;color:#444">Lorem ipsum dolor sit amet, consectetur adipiscing elit. Est vitae, pellentesque cum in etiam ultrices. Neque egestas velit facilisis at dolor at. Accumsan, arcu massa tellus tempus, aenean purus viverra. Commodo sed mauris ultrices quam urna.</p>
<div class="abs tabs"><span class="active">Web Application</span><span>Mobile App</span><span>CMS Websites</span><span>E Commerce Website</span></div>
<div class="abs shot" style="left:115px;background:linear-gradient(135deg,#ffffff 40%,#1b2440 60%,#d9f1f0)" role="img" aria-label="Web application project screenshots"></div>
<div class="abs shot" style="left:363px;background:linear-gradient(135deg,#f5f0fa,#ffffff 50%,#e8d8ef)" role="img" aria-label="Wellness website project screenshots"></div>
<div class="abs shot" style="left:614px;background:linear-gradient(135deg,#F0912C 15%,#ffffff 30%,#1a1f3a 60%)" role="img" aria-label="Cyber security website project screenshots"></div>
<div class="abs shot" style="left:861px;background:linear-gradient(135deg,#34c6a8 15%,#ffffff 35%,#7a2424 65%,#ffffff)" role="img" aria-label="Construction company website project screenshots"></div>
<div class="abs arrows">
  <svg width="30" height="16" viewBox="0 0 30 16"><path d="M29 8H2M8 2 2 8l6 6" stroke="#444" stroke-width="2" fill="none"/></svg>
  <svg width="30" height="16" viewBox="0 0 30 16"><path d="M1 8h27M22 2l6 6-6 6" stroke="#444" stroke-width="2" fill="none"/></svg>
</div>

<!-- Contact -->
<div class="abs grid" style="left:625px;top:3575px;width:330px;height:330px"></div>
<h2 class="abs contact-title">Contact Our<br>Experts Right Now</h2>
<p class="abs contact-text">Lorem ipsum dolor sit amet, consectetur adipiscing elit. Est vitae, pellentesque cum in etiam ultrices. Neque egestas velit facilisis at dolor at. Accumsan, arcu massa tellus tempus, aenean purus viverra.</p>
<a class="abs btn btn-orange contact-btn">Contact Our Team</a>
<div class="abs photo c-photo-1" role="img" aria-label="Smiling man in front of a whiteboard with sticky notes"></div>
<div class="abs photo c-photo-2" role="img" aria-label="Woman working on a laptop in a bright room"></div>

<!-- Footer -->
<footer class="abs footer">
  <div class="abs f-brand"><div class="brand-name">MAVORIX</div><div class="brand-sub">Communications Ltd</div></div>
  <p class="abs f-tag">Lorem ipsum dolor sit amet, consectetur adipiscing elit. Est vitae, pellentesque cum</p>
  <div class="abs f-col" style="left:576px;top:66px"><h4>Quick</h4><a>Home</a><a>About Us</a><a>Services</a><a>Portfolio</a><a>Contact Us</a></div>
  <div class="abs f-col" style="left:741px;top:66px"><h4>Our Services</h4><a>Software Development</a><a>UX Design</a><a>Mobile App</a><a>SEO</a></div>
  <div class="abs f-col" style="left:987px;top:66px"><h4>Legal</h4><a>Legal</a><a>Privacy Policy</a><a>Terms</a><a>Cookies Policy</a></div>
</footer>
<p class="abs copy">©Copyright 2022. <u>Mavorix Communications Ltd</u> | All Rights Reserved</p>
<div class="abs social"><i></i><i></i><i></i><i></i></div>

</body>
</html>
```